Simple and Clean business card design

We would like the design to be simple clean and to incorporate our colors.

We are open to your design and talent, we have the dots in our logo as we think of it as data points and we connect data points for people.

We are open to see the great creative and clean design you bring to the table

Contact Information for Business Card

please include: name, position, email, phone and website

Font styles to use
Sans Serif

Requirements
Must have
• my colors incorporated, simplicity
Nice to have
• lots of white space, simplicity
Should not have
• complexicity/ complex art

```html
<!DOCTYPE html>
<html lang="en">
<head>
<meta charset="utf-8">
<title>Nectaro Business Card</title>
<link rel="stylesheet" href="https://fonts.googleapis.com/css2?family=Jost:wght@400;500;700&display=swap">
<style>
  :root {
    --backdrop: #dcdcdc;
    --card: #ffffff;
    --ink: #151515;
    --text: #333333;
    --green: #2ea852;
    --yellow: #f8bd16;
    --blue: #5f87c8;
  }
  * { box-sizing: border-box; margin: 0; padding: 0; }
  html, body {
    width: 1200px; height: 1017px; overflow: hidden;
    background: var(--backdrop);
    font-family: "Jost", "Futura", sans-serif;
  }
  .card {
    position: absolute;
    left: 278px;
    width: 644px; height: 368px;
    background: var(--card);
    border-radius: 26px;
    overflow: hidden;
  }
  .card--front { top: 97px; }
  .card--back { top: 519px; }

  .wordmark {
    position: absolute;
    display: flex; align-items: center; gap: 10px;
    color: var(--ink);
    font-weight: 500;
    line-height: 1;
  }
  .wordmark__dot { border-radius: 50%; background: var(--blue); flex: none; }
  .card--front .wordmark { left: 26px; top: 62px; font-size: 58px; }
  .card--front .wordmark__dot { width: 14px; height: 14px; }
  .card--back .wordmark {
    left: 50%; top: 50%; transform: translate(-50%, -50%);
    font-size: 112px; gap: 18px;
  }
  .card--back .wordmark__dot { width: 24px; height: 24px; }

  .identity {
    position: absolute; right: 27px; top: 44px;
    text-align: right;
  }
  .identity__company {
    color: var(--green);
    font-weight: 700; font-size: 23px; letter-spacing: 0.5px;
    line-height: 1.1;
  }
  .identity__role {
    color: var(--text);
    font-size: 16px; margin-top: 3px;
  }
  .accent-bar {
    position: absolute; left: 630px; top: 48px;
    width: 14px; height: 38px;
    background: var(--yellow);
  }

  .contacts {
    position: absolute; left: 27px; top: 266px;
    list-style: none;
  }
  .contacts li {
    display: flex; align-items: center; gap: 7px;
    height: 23.5px;
    color: var(--text); font-size: 16.5px;
  }
  .contacts svg { width: 13px; height: 13px; flex: none; }
</style>
</head>
<body>
  <section class="card card--front">
    <div class="wordmark"><span class="wordmark__name">Nectaro</span><span class="wordmark__dot"></span></div>

    <div class="identity">
      <div class="identity__company">NECTARO.ONE</div>
      <div class="identity__role">Founder/ CEO</div>
    </div>
    <div class="accent-bar"></div>

    <ul class="contacts">
      <li>
        <svg viewBox="0 0 16 16" aria-hidden="true"><path fill="var(--green)" d="M3.6 1.5 6 4.2 4.7 5.7c.9 2 2.5 3.6 4.5 4.6l1.5-1.3 2.8 2.4-1.6 2.2C7 13.3 2.7 9 1.5 3.2z"/><path fill="none" stroke="var(--green)" stroke-width="1.3" d="M9 2.5a4.5 4.5 0 0 1 4.5 4.5M9 5a2 2 0 0 1 2 2"/></svg>
        555-014-2290
      </li>
      <li>
        <svg viewBox="0 0 16 16" aria-hidden="true"><rect x="1" y="3" width="14" height="10" fill="var(--green)"/><path fill="none" stroke="#fff" stroke-width="1.2" d="M1 3l7 5.5L15 3M1 13l5-4.5M15 13l-5-4.5"/></svg>
        mara.lind@nectaro.one
      </li>
      <li>
        <svg viewBox="0 0 16 16" aria-hidden="true"><circle cx="8" cy="8" r="7" fill="var(--green)"/><path fill="#fff" d="M4 4.5c1.5-.5 2.5.5 2.2 1.8-.3 1.2 1.2 1.5 1 2.8-.2 1.3-1.6 1.2-2 2.6C3.8 10.8 3 8 4 4.5zM10 3.5c1.5.6 2.5 2 2.6 3.5-1 .3-1.8-.4-2.3-1.3-.4-.8-.6-1.6-.3-2.2z"/></svg>
        www.Nectaro.one
      </li>
    </ul>
  </section>

  <section class="card card--back">
    <div class="wordmark"><span class="wordmark__name">Nectaro</span><span class="wordmark__dot"></span></div>
  </section>
</body>
</html>
```